Proposal for a new Label - Proposal for a new Label

New design for label, renewal of existing label for more than 10 years, we want to change the image of the label, highlighting the name KVR-M3 and giving more notoriety to the brand, keeping the rest of the information on the label, changing the location , color tone and tone, you can vary the tone of the colors, a stronger or softer orange, a darker or lighter gray, the corporate colors recognized by customers are white, orange and gray. The product is a powder additive that is used in the extraction of copper, the base is a bag of Kraf paper of 25 Kg. This product has been awarded as an innovative product, which marked a precedent in the mining industry positively impacting the quality of the copper produced. New design for label, renew existing label for more than 10 years, we want to change the image of the label, highlighting the name KVR-M3 and giving more notoriety to the brand, keeping the rest of the information on the label, changing location , font. and hue of colors, being able to be a stronger orange or a darker gray or vice versa, the corporate colors recognized by the clients are white, orange and gray. The product is a powder additive that is used in copper mining, the base is a bag of Kraf paper of 25 Kg. This product has been awarded as an innovative product, which is marked in the mining industry impacting the quality of copper produced.

Target Market(s)

Mining - Mining

Colors
f04a50
ec1f27
f59296
f68e4d
f37122
f8ba93
757575
cfcfcf
c4c4c4

Requirements
Must have
• 217mm X 330mm Highlight the brand Highlight the brand
Nice to have
• At the base of the label place the flags of the mining countries where the additive is used: Chile, Peru, Mexico, Spain, DR Congo, Zambia, Laos, Kazakhstan, Australia. At the base of the label, place the flags of the mining countries where the additive is used: Chile, Peru, Mexico, Spain, Congo DRC, Zambia, Laos, Kazakhstan, Australia. Indicate in a corner or place on the label that it is a global product. Indicate in a corner or place on the label that is a global product.

```html
<!DOCTYPE html>
<html lang="es">
<head>
<meta charset="utf-8">
<title>KVR-M3 Label</title>
<link href="https://fonts.googleapis.com/css2?family=Audiowide&family=Roboto+Condensed:wght@400;700&family=Roboto:wght@400;700;900&display=swap" rel="stylesheet">
<style>
:root{
  --orange:#c96535;
  --orange-light:#e0926a;
  --white:#ffffff;
  --gray:#757575;
  --gray-dark:#4a4a4a;
  --gray-frame:#6e6e6e;
  --navy:#0d2a5c;
  --bronze:#c9825a;
  --page:#ffffff;
}
*{box-sizing:border-box;margin:0;padding:0}
html,body{width:928px;height:1200px;overflow:hidden;background:var(--page)}
body{position:relative;font-family:"Roboto",Arial,sans-serif}
.label{position:absolute;left:12px;width:908px;height:568px;background:var(--orange);border-radius:28px}
.label--es{top:20px}
.label--en{top:615px}
.brand{position:absolute;left:180px;top:30px;display:flex;align-items:center;gap:10px;color:var(--white);font-family:"Roboto Condensed",sans-serif;font-weight:700;font-size:24px;letter-spacing:1px}
.brand-dot{width:34px;height:34px;border-radius:50%;background:var(--white)}
.company{position:absolute;left:568px;top:16px;color:var(--white);font-family:"Roboto",sans-serif;font-weight:700;font-size:12.5px;line-height:15px}
.product-name{position:absolute;left:56px;top:100px;width:800px;color:var(--white);font-family:"Audiowide",sans-serif;font-size:116px;line-height:110px;letter-spacing:24px;white-space:nowrap}
.band{position:absolute;left:56px;top:228px;width:492px;height:40px;background:var(--orange-light)}
.subtitle{position:absolute;left:568px;top:228px;width:286px;height:40px;border-top:2px solid var(--white);border-bottom:2px solid var(--white);color:var(--white);font-family:"Roboto Condensed",sans-serif;font-weight:700;font-size:28px;line-height:36px;white-space:nowrap}
.subtitle--spaced{letter-spacing:5.5px}
.panel{position:absolute;left:10px;top:283px;width:888px;height:274px;background:var(--white);border-radius:24px}
.field{position:absolute;left:20px;width:170px;height:48px;background:var(--gray-frame);border-radius:6px;padding:2px 3px 3px}
.field-title{color:var(--white);font-size:13px;text-align:center;line-height:15px}
.field-input{height:27px;background:var(--white);border-radius:4px;margin-top:1px}
.global{position:absolute;left:20px;top:206px;width:170px;height:56px;background:var(--navy);border-radius:6px;display:flex;align-items:center;gap:10px;padding-left:10px;color:var(--white);font-size:12.5px;line-height:15px}
.global b{font-weight:700}
.notice{position:absolute;left:218px;top:22px;width:226px;height:50px;border-top:1px solid var(--orange);border-bottom:1px solid var(--orange);font-family:"Roboto Condensed",sans-serif;font-weight:700;font-size:10.5px;line-height:14px;color:var(--gray-dark);text-align:center;padding-top:4px}
.weight-label{position:absolute;left:218px;top:86px;font-family:"Roboto Condensed",sans-serif;font-weight:700;font-size:12px;letter-spacing:4px;color:var(--gray)}
.weight{position:absolute;left:214px;top:96px;font-family:"Roboto Condensed",sans-serif;font-weight:700;font-size:96px;line-height:100px;color:var(--gray);letter-spacing:-1px}
.icons{position:absolute;left:470px;top:14px;width:56px}
.icons svg{display:block;margin-bottom:14px}
.safety{position:absolute;left:558px;top:22px;width:280px;font-family:"Roboto Condensed",sans-serif;font-weight:700;font-size:12px;line-height:14px;color:var(--gray-dark)}
.safety h3{font-size:12px;font-weight:700}
.safety .gap{height:12px}
.aid{position:relative;padding-left:0}
.aid::before{content:"!";display:inline-block;width:10px;height:10px;border-radius:50%;background:var(--orange);color:var(--white);font-size:8px;line-height:10px;text-align:center;margin-right:3px;vertical-align:1px}
.award{position:absolute;left:798px;top:14px;width:72px;height:72px;border-radius:50%;background:var(--bronze);border:4px solid var(--white);box-shadow:0 0 0 1.5px var(--bronze)}
.flags{position:absolute;left:216px;top:234px;display:flex;gap:26.5px}
.flags svg{display:block;width:46px;height:30px}
</style>
</head>
<body>

<!-- Spanish label -->
<section class="label label--es">
  <div class="brand"><span class="brand-dot"></span>NORANDE METALLURGY</div>
  <address class="company">SOCIEDAD NORTE ANDINO LTDA.<br>Calle Los Aromos 215 Galpón 14<br>Barrio Industrial Antofagasta<br>ANTOFAGASTA, CHILE<br>Fono: 56-55-2740113 / 56-55-2740114</address>
  <h1 class="product-name">KVR-M3</h1>
  <div class="band" role="img" aria-label="Banda decorativa de líneas diagonales"></div>
  <h2 class="subtitle">REFINADOR DE GRANO</h2>
  <div class="panel">
    <div class="field" style="top:22px"><div class="field-title">Lote Número:</div><div class="field-input"></div></div>
    <div class="field" style="top:79px"><div class="field-title">Fecha de Fabricación:</div><div class="field-input"></div></div>
    <div class="field" style="top:136px"><div class="field-title">Fecha de Vencimiento:</div><div class="field-input"></div></div>
    <div class="global">
      <svg width="36" height="36" viewBox="0 0 36 36" fill="none" stroke="#fff" stroke-width="2"><circle cx="18" cy="18" r="15"/><ellipse cx="18" cy="18" rx="7" ry="15"/><line x1="3" y1="18" x2="33" y2="18"/><line x1="18" y1="3" x2="18" y2="33"/><path d="M6 10h24M6 26h24"/></svg>
      <span>Producto de<br><b>Exportación Global</b></span>
    </div>
    <p class="notice">PRODUCTO NO CLASIFICADO COMO<br>PELIGROSO, DE ACUERDO A<br>LA LEGISLACIÓN DE TRANSPORTE</p>
    <div class="weight-label">Peso Neto:</div>
    <div class="weight">25 Kg</div>
    <div class="icons">
      <svg width="56" height="54" viewBox="0 0 56 54" fill="none" stroke-width="2.5"><path d="M6 4l-1 3M16 4l-1 3M26 4l-1 3M36 4l-1 3M46 4l-1 3M11 10l-1 3M21 10l-1 3M31 10l-1 3M41 10l-1 3" stroke="#0d2a5c" stroke-width="1.5"/><path d="M6 32 Q28 8 50 32 Q44 27 39 32 Q33 27 28 32 Q22 27 17 32 Q11 27 6 32Z" stroke="#c96535"/><path d="M28 32v14a4 4 0 0 1-8 0" stroke="#c96535"/></svg>
      <svg width="56" height="54" viewBox="0 0 56 54" fill="none" stroke-width="3"><path d="M4 20L28 4l24 16" stroke="#0d2a5c"/><rect x="14" y="22" width="26" height="12" stroke="#c96535" stroke-width="2.5"/><path d="M14 22l6-5h26l-6 5M40 34l6-5V17" stroke="#c96535" stroke-width="2.5"/><path d="M4 40h48M4 48h48" stroke="#0d2a5c"/></svg>
      <svg width="56" height="54" viewBox="0 0 56 54" fill="none" stroke-width="2.5"><circle cx="24" cy="30" r="9" stroke="#c96535"/><path d="M24 12v5M24 43v5M6 30h5M37 30h3M11 17l4 4M11 43l4-4M37 17l-4 4M37 43l-4-4" stroke="#c96535"/><path d="M46 6v46" stroke="#0d2a5c" stroke-width="3"/></svg>
    </div>
    <div class="safety">
      <h3>INFORMACIÓN DE SEGURIDAD:</h3>
      - Evitar el contacto con la piel.<br>
      - Evitar inhalar los polvos.<br>
      - Usar protección adecuada.<br>
      - Almacenar en lugar freco y ventilado.<br>
      - Derrames: recoger con material absorbente.<br>
      - Incendios: usar extintores a base de polvo químico Co2, espuma o agua.
      <div class="gap"></div>
      <h3>PRIMEROS AUXILIOS:</h3>
      <div class="aid">Contacto con los ojos: lavar con abundante agua por lo menos durante 15 minutos.</div>
      <div class="aid">Contacto con la piel: lavar con mucha agua y jabón.</div>
    </div>
    <div class="award" role="img" aria-label="Distintivo de premio a la innovación"></div>
    <div class="flags">
      <svg viewBox="0 0 46 30" role="img" aria-label="Chile"><rect width="46" height="30" fill="#d52b1e"/><rect width="46" height="15" fill="#fff"/><rect width="16" height="15" fill="#0039a6"/><circle cx="8" cy="7.5" r="2.5" fill="#fff"/></svg>
      <svg viewBox="0 0 46 30" role="img" aria-label="Perú"><rect width="46" height="30" fill="#d91023"/><rect x="15.3" width="15.4" height="30" fill="#fff"/></svg>
      <svg viewBox="0 0 46 30" role="img" aria-label="México"><rect width="46" height="30" fill="#ce1126"/><rect width="15.3" height="30" fill="#006847"/><rect x="15.3" width="15.4" height="30" fill="#fff"/></svg>
      <svg viewBox="0 0 46 30" role="img" aria-label="España"><rect width="46" height="30" fill="#c60b1e"/><rect y="7.5" width="46" height="15" fill="#ffc400"/></svg>
      <svg viewBox="0 0 46 30" role="img" aria-label="RD Congo"><rect width="46" height="30" fill="#007fff"/><path d="M0 26L40 0h6v4L6 30H0z" fill="#f7d618"/><path d="M0 28L43 0h3v2L3 30H0z" fill="#ce1021"/><path d="M5 3l1 2.5h2.5l-2 1.5 1 2.5-2.5-1.5-2 1.5 1-2.5-2-1.5h2.5z" fill="#f7d618"/></svg>
      <svg viewBox="0 0 46 30" role="img" aria-label="Zambia"><rect width="46" height="30" fill="#198a00"/><rect x="30" y="12" width="5" height="18" fill="#de2010"/><rect x="35" y="12" width="5" height="18" fill="#000"/><rect x="40" y="12" width="6" height="18" fill="#ef7d00"/></svg>
      <svg viewBox="0 0 46 30" role="img" aria-label="Laos"><rect width="46" height="30" fill="#ce1126"/><rect y="7.5" width="46" height="15" fill="#002868"/><circle cx="23" cy="15" r="6" fill="#fff"/></svg>
      <svg viewBox="0 0 46 30" role="img" aria-label="Australia"><rect width="46" height="30" fill="#00247d"/><path d="M0 0l23 15M23 0L0 15" stroke="#fff" stroke-width="3"/><path d="M11.5 0v15M0 7.5h23" stroke="#fff" stroke-width="4"/><path d="M11.5 0v15M0 7.5h23" stroke="#cf142b" stroke-width="2"/><circle cx="11.5" cy="23" r="2.5" fill="#fff"/><circle cx="35" cy="7" r="1.5" fill="#fff"/><circle cx="30" cy="15" r="1.5" fill="#fff"/><circle cx="40" cy="13" r="1.5" fill="#fff"/><circle cx="35" cy="25" r="1.5" fill="#fff"/></svg>
      <svg viewBox="0 0 46 30" role="img" aria-label="Kazajistán"><rect width="46" height="30" fill="#00afca"/><circle cx="23" cy="13" r="5" fill="#fec50c"/><rect x="3" y="3" width="2" height="24" fill="#fec50c"/></svg>
    </div>
  </div>
</section>

<!-- English label -->
<section class="label label--en">
  <div class="brand"><span class="brand-dot"></span>NORANDE METALLURGY</div>
  <address class="company">SOCIEDAD NORTE ANDINO LTDA.<br>Calle Los Aromos 215 Galpón 14<br>Barrio Industrial Antofagasta<br>ANTOFAGASTA, CHILE<br>Fono: 56-55-2740113 / 56-55-2740114</address>
  <h1 class="product-name">KVR-M3</h1>
  <div class="band" role="img" aria-label="Decorative band of diagonal lines"></div>
  <h2 class="subtitle subtitle--spaced">GRAIN REFINER</h2>
  <div class="panel">
    <div class="field" style="top:22px"><div class="field-title">Lot Number:</div><div class="field-input"></div></div>
    <div class="field" style="top:79px"><div class="field-title">Date of Manufacture</div><div class="field-input"></div></div>
    <div class="field" style="top:136px"><div class="field-title">Date of Expiration</div><div class="field-input"></div></div>
    <div class="global">
      <svg width="36" height="36" viewBox="0 0 36 36" fill="none" stroke="#fff" stroke-width="2"><circle cx="18" cy="18" r="15"/><ellipse cx="18" cy="18" rx="7" ry="15"/><line x1="3" y1="18" x2="33" y2="18"/><line x1="18" y1="3" x2="18" y2="33"/><path d="M6 10h24M6 26h24"/></svg>
      <span><b>Global Exportation</b><br>Product</span>
    </div>
    <p class="notice">PRODUCT NOT CLASIFICATED AS<br>DANGEROUS, ACCORDING TO<br>THE TRANSPORT LEGISLATION</p>
    <div class="weight-label">Net Weight:</div>
    <div class="weight">25 Kg</div>
    <div class="icons">
      <svg width="56" height="54" viewBox="0 0 56 54" fill="none" stroke-width="2.5"><path d="M6 4l-1 3M16 4l-1 3M26 4l-1 3M36 4l-1 3M46 4l-1 3M11 10l-1 3M21 10l-1 3M31 10l-1 3M41 10l-1 3" stroke="#0d2a5c" stroke-width="1.5"/><path d="M6 32 Q28 8 50 32 Q44 27 39 32 Q33 27 28 32 Q22 27 17 32 Q11 27 6 32Z" stroke="#c96535"/><path d="M28 32v14a4 4 0 0 1-8 0" stroke="#c96535"/></svg>
      <svg width="56" height="54" viewBox="0 0 56 54" fill="none" stroke-width="3"><path d="M4 20L28 4l24 16" stroke="#0d2a5c"/><rect x="14" y="22" width="26" height="12" stroke="#c96535" stroke-width="2.5"/><path d="M14 22l6-5h26l-6 5M40 34l6-5V17" stroke="#c96535" stroke-width="2.5"/><path d="M4 40h48M4 48h48" stroke="#0d2a5c"/></svg>
      <svg width="56" height="54" viewBox="0 0 56 54" fill="none" stroke-width="2.5"><circle cx="24" cy="30" r="9" stroke="#c96535"/><path d="M24 12v5M24 43v5M6 30h5M37 30h3M11 17l4 4M11 43l4-4M37 17l-4 4M37 43l-4-4" stroke="#c96535"/><path d="M46 6v46" stroke="#0d2a5c" stroke-width="3"/></svg>
    </div>
    <div class="safety">
      <h3>SAFETY INFORMATION:</h3>
      - Avoid contact with skin.<br>
      - Avoid breathing dust.<br>
      - Use proper protection.<br>
      - Store in a cool and ventilated place.<br>
      - Spills: pick up with absorbent material.<br>
      - Fire: extinguishers should use dry chemical, CO2, foam or water.
      <div class="gap"></div>
      <h3>FIRST AIDS:</h3>
      <div class="aid">Eye contact: wash with abundant water at least for 15 minutes.</div>
      <div class="aid">Skin contact: wash with soap and water.</div>
    </div>
    <div class="award" role="img" aria-label="Innovation award badge"></div>
    <div class="flags">
      <svg viewBox="0 0 46 30" role="img" aria-label="Chile"><rect width="46" height="30" fill="#d52b1e"/><rect width="46" height="15" fill="#fff"/><rect width="16" height="15" fill="#0039a6"/><circle cx="8" cy="7.5" r="2.5" fill="#fff"/></svg>
      <svg viewBox="0 0 46 30" role="img" aria-label="Peru"><rect width="46" height="30" fill="#d91023"/><rect x="15.3" width="15.4" height="30" fill="#fff"/></svg>
      <svg viewBox="0 0 46 30" role="img" aria-label="Mexico"><rect width="46" height="30" fill="#ce1126"/><rect width="15.3" height="30" fill="#006847"/><rect x="15.3" width="15.4" height="30" fill="#fff"/></svg>
      <svg viewBox="0 0 46 30" role="img" aria-label="Spain"><rect width="46" height="30" fill="#c60b1e"/><rect y="7.5" width="46" height="15" fill="#ffc400"/></svg>
      <svg viewBox="0 0 46 30" role="img" aria-label="DR Congo"><rect width="46" height="30" fill="#007fff"/><path d="M0 26L40 0h6v4L6 30H0z" fill="#f7d618"/><path d="M0 28L43 0h3v2L3 30H0z" fill="#ce1021"/><path d="M5 3l1 2.5h2.5l-2 1.5 1 2.5-2.5-1.5-2 1.5 1-2.5-2-1.5h2.5z" fill="#f7d618"/></svg>
      <svg viewBox="0 0 46 30" role="img" aria-label="Zambia"><rect width="46" height="30" fill="#198a00"/><rect x="30" y="12" width="5" height="18" fill="#de2010"/><rect x="35" y="12" width="5" height="18" fill="#000"/><rect x="40" y="12" width="6" height="18" fill="#ef7d00"/></svg>
      <svg viewBox="0 0 46 30" role="img" aria-label="Laos"><rect width="46" height="30" fill="#ce1126"/><rect y="7.5" width="46" height="15" fill="#002868"/><circle cx="23" cy="15" r="6" fill="#fff"/></svg>
      <svg viewBox="0 0 46 30" role="img" aria-label="Australia"><rect width="46" height="30" fill="#00247d"/><path d="M0 0l23 15M23 0L0 15" stroke="#fff" stroke-width="3"/><path d="M11.5 0v15M0 7.5h23" stroke="#fff" stroke-width="4"/><path d="M11.5 0v15M0 7.5h23" stroke="#cf142b" stroke-width="2"/><circle cx="11.5" cy="23" r="2.5" fill="#fff"/><circle cx="35" cy="7" r="1.5" fill="#fff"/><circle cx="30" cy="15" r="1.5" fill="#fff"/><circle cx="40" cy="13" r="1.5" fill="#fff"/><circle cx="35" cy="25" r="1.5" fill="#fff"/></svg>
      <svg viewBox="0 0 46 30" role="img" aria-label="Kazakhstan"><rect width="46" height="30" fill="#00afca"/><circle cx="23" cy="13" r="5" fill="#fec50c"/><rect x="3" y="3" width="2" height="24" fill="#fec50c"/></svg>
    </div>
  </div>
</section>

</body>
</html>
```